Design eines Zertifikats
Ich bin total begeistert. Super Kommunikation, super schnelle Reaktion auf kleine Änderungswünsche, ich bin wirklich rundum zufrieden!! Auch bei weiterführenden Fragen die gar nicht direkt mit dem Design zusammenhingen wurde mir total schnell und sympathisch geholfen, ich kann die Designerin nur wärmstens weiterempfehlen!
Zielgruppe
Ich betreibe einen Onlineshop, in dem ich sogenannte Sterntaufen verkaufe. Ein Kunde bekommt dabei im Zuge seines Kaufes ein Zertifikat ausgestellt mit Daten zu seinem getauften Stern. Es geht hier um das Design eines neuen Zertifikats um möglichst noch mehr Käufer anzusprechen. Es sind bereits 3 Designs vorhanden, das neue sollte sich entsprechend etwas absetzen.
Ich lasse die Zertifikate in einer Druckerei drucken, und bedrucke diese dann selber mit den Daten der Sterntaufe, es muss auf dem Zertifikat also ein heller Bereich vorhanden sein in dem ich drucken kann.
Aufgabenstellung
Das Zertifikat soll A4 sein. Es sollte modern sein und sich wie gesagt möglichst von den bestehenden absetzen, und ein möglichst breites Publikum ansprechen.
Beispiele für Zertifikate der Konkurrenz finden sich unter:
lichtpunkt-shop.de
nebelbuchung.de
himmelsgabe-online.de
Das von lichtpunkt-shop.de gefällt mir persönlich ganz gut, aber lasst euch nicht von den Vorschlägen einschränken.
Bitte nicht zu exzessiv kostenpflichtiges Stockmaterial verwenden, ich mache leider aktuell noch Miese mit dem Shop :-)
Bitte schaut auf meine Webseite um ein Gefühl dafür zu bekommen wie viel Platz für Text vorhanden sein muss.

```html
<!DOCTYPE html>
<html lang="de">
<head>
<meta charset="utf-8">
<title>Sternurkunde</title>
<link rel="stylesheet" href="https://fonts.googleapis.com/css2?family=Playfair+Display:wght@400;700&display=swap">
<style>
  :root {
    --navy: #252c6a;
    --white: #ffffff;
    --paper: #f4f4f5;
    --paper-shade: #e4e4e7;
    --gold-light: #ecd27e;
    --gold-dark: #a07a2c;
    --sky-top: #1c2556;
    --sky-mid: #3a3f8f;
    --sky-bottom: #4a2a62;
  }
  html, body {
    margin: 0;
    padding: 0;
    overflow: hidden;
    background: #ffffff;
  }
  .certificate {
    position: relative;
    width: 1200px;
    height: 849px;
    overflow: hidden;
    font-family: "Playfair Display", Georgia, serif;
    color: var(--navy);
  }
  .night-sky {
    position: absolute;
    inset: 0;
    background:
      radial-gradient(ellipse 520px 220px at 260px 560px, rgba(120,130,220,0.55), transparent 70%),
      linear-gradient(160deg, var(--sky-top) 0%, var(--sky-mid) 55%, var(--sky-bottom) 100%);
  }
  .paper-shape {
    position: absolute;
    inset: 0;
  }
  .title {
    position: absolute;
    left: 85px;
    top: 62px;
    margin: 0;
    font-weight: 400;
    font-size: 78px;
    line-height: 1;
    color: var(--white);
  }
  .seal {
    position: absolute;
    left: 805px;
    top: 150px;
    width: 156px;
    height: 156px;
  }
  .heading {
    position: absolute;
    left: 683px;
    width: 400px;
    text-align: center;
    font-weight: 700;
    font-size: 20px;
    margin: 0;
  }
  .heading--star { top: 364px; }
  .heading--named { top: 551px; }
  .star-name {
    position: absolute;
    left: 683px;
    width: 400px;
    top: 604px;
    text-align: center;
    font-weight: 700;
    font-size: 37px;
    letter-spacing: 2px;
    margin: 0;
  }
  .data-row {
    position: absolute;
    left: 0;
    display: flex;
    font-size: 18px;
    line-height: 1;
  }
  .data-row dt {
    width: 864px;
    text-align: right;
    margin: 0;
  }
  .data-row dd {
    margin: 0 0 0 37px;
  }
  dl { margin: 0; }
</style>
</head>
<body>
<main class="certificate">
  <div class="night-sky" role="img" aria-label="Foto eines Sternenhimmels mit der Milchstraße in Blau- und Violetttönen"></div>

  <svg class="paper-shape" width="1200" height="849" viewBox="0 0 1200 849" aria-hidden="true">
    <defs>
      <linearGradient id="paperFill" x1="0" y1="0" x2="1" y2="1">
        <stop offset="0" stop-color="#e9e9ec"/>
        <stop offset="0.5" stop-color="#f7f7f8"/>
        <stop offset="1" stop-color="#ececee"/>
      </linearGradient>
      <linearGradient id="goldBand" x1="0" y1="0" x2="0" y2="1">
        <stop offset="0" stop-color="#f2db8c"/>
        <stop offset="0.5" stop-color="#d2ad58"/>
        <stop offset="1" stop-color="#9c7629"/>
      </linearGradient>
    </defs>
    <path d="M 872 0 C 600 120 430 450 418 849 L 1200 849 L 1200 0 Z" fill="url(#paperFill)"/>
    <path d="M 872 0 C 600 120 430 450 418 849" fill="none" stroke="url(#goldBand)" stroke-width="18"/>
  </svg>

  <h1 class="title">Sternurkunde</h1>

  <svg class="seal" viewBox="0 0 156 156" aria-hidden="true">
    <circle cx="78" cy="78" r="76" fill="var(--navy)"/>
    <circle cx="78" cy="78" r="64" fill="none" stroke="#ffffff" stroke-width="4"/>
  </svg>

  <h2 class="heading heading--star">Der Stern mit den Daten</h2>

  <dl>
    <div class="data-row" style="top:424px"><dt>HIP-No.</dt><dd>11767</dd></div>
    <div class="data-row" style="top:451px"><dt>Rektamension</dt><dd>02h 31m 47.08s</dd></div>
    <div class="data-row" style="top:478px"><dt>Deklination</dt><dd>+89° 15' 50.9'</dd></div>
    <div class="data-row" style="top:505px"><dt>Scheinbare Magnitude</dt><dd>1,97</dd></div>
  </dl>

  <h2 class="heading heading--named">wurde auf der Namen getauft</h2>

  <p class="star-name">Maria</p>

  <dl>
    <div class="data-row" style="top:683px"><dt>Taufdatum</dt><dd>14.02.2020</dd></div>
    <div class="data-row" style="top:710px"><dt>Registrationsnummer</dt><dd>xxx-xxx-xxx-xxx</dd></div>
  </dl>
</main>
</body>
</html>
```